shutter business card and postcard design

Custom Interior and Exterior Shutters manufactured In Houston Texas Made in USA we offer fast delivery lifetime warranty
Dale Whitcombe owner has been manufacturing shutters in houston for over 44 years
nedd to use one of the pictures provided and add company name phone number on face Louver Crest (281)555-7384
back side
louver crest
2317 quillfeather ln.
houston, texas 77999
email louvercrest@mailnest.example
website louvercresthouston.example

```html
<!DOCTYPE html>
<html lang="en">
<head>
<meta charset="utf-8">
<title>Louver Crest Postcard</title>
<link rel="stylesheet" href="https://fonts.googleapis.com/css2?family=Montserrat:wght@500;600;700;800&family=Roboto+Condensed:wght@400;700&display=swap">
<style>
  :root {
    --bg: #5b3522;
    --paper: #ffffff;
    --ink: #222222;
    --panel-dark: #2a2322;
    --brand-orange: #f0a21c;
    --phone-red: #d9261c;
    --band-red: #a3352b;
    --highlight: #f4e46a;
    --cream: #fbeec0;
    --rule: #9a9a9a;
    --photo-a: #8a8f8c;
    --photo-b: #4b4f4c;
  }
  * { box-sizing: border-box; margin: 0; padding: 0; }
  html, body { width: 1200px; height: 1000px; overflow: hidden; }
  body { background: var(--bg); position: relative; font-family: "Roboto Condensed", sans-serif; color: var(--ink); }

  .card { position: absolute; background: var(--paper); overflow: hidden; box-shadow: 0 4px 14px rgba(0,0,0,.35); }
  .card--front { left: 25px; top: 25px; width: 680px; height: 453px; }
  .card--back { left: 470px; top: 517px; width: 680px; height: 455px; }

  .brand-name { font-family: "Montserrat", sans-serif; font-weight: 800; color: var(--brand-orange); letter-spacing: -1px; line-height: 1; }
  .brand-tagline { font-family: "Montserrat", sans-serif; font-weight: 500; color: var(--ink); line-height: 1; }

  /* front */
  .front-header .brand-name { position: absolute; left: 28px; top: 34px; font-size: 40px; }
  .front-header .brand-tagline { position: absolute; left: 30px; top: 78px; font-size: 16px; }
  .front-contact { position: absolute; right: 36px; top: 22px; text-align: center; font-family: "Montserrat", sans-serif; }
  .front-contact .cta { font-size: 14.5px; font-weight: 500; }
  .front-contact .phone { font-size: 38px; font-weight: 700; color: var(--phone-red); line-height: 1.15; letter-spacing: -.5px; }
  .front-contact .web { font-size: 14.5px; font-weight: 500; }
  .front-contact .web span { color: var(--phone-red); }

  .front-panel { position: absolute; left: 0; top: 108px; width: 680px; height: 345px; background: var(--panel-dark); }
  .front-photo { position: absolute; left: 285px; top: 0; width: 395px; height: 345px; background: linear-gradient(160deg, #9fa39f 0%, var(--photo-a) 35%, #a0704a 70%, var(--photo-b) 100%); }
  .front-curve { position: absolute; left: 0; top: 0; }
  .front-copy { position: absolute; left: 24px; top: 18px; width: 275px; color: #fff; font-size: 13.5px; line-height: 1.33; text-align: justify; }
  .front-copy p + p { margin-top: 14px; }
  .front-divider { position: absolute; left: 24px; top: 246px; width: 252px; border-top: 1.5px dashed #fff; }
  .front-warranty { position: absolute; left: 24px; top: 258px; color: #fff; font-size: 14px; text-transform: uppercase; line-height: 1.3; }
  .front-warranty strong { color: var(--highlight); }

  /* back */
  .back-photo { position: absolute; left: 0; top: 0; width: 337px; height: 185px; background: linear-gradient(170deg, #8a9694 0%, #6f7b78 50%, #5a4236 100%); }
  .back-band { position: absolute; left: 0; top: 185px; width: 337px; height: 98px; background: var(--band-red); color: #fff; padding: 9px 0 0 26px; }
  .back-band h3 { font-weight: 400; font-size: 16px; margin-bottom: 4px; }
  .benefit-list { list-style: none; }
  .benefit-list li { font-weight: 700; font-size: 12.5px; color: var(--cream); line-height: 1.27; display: flex; align-items: center; gap: 3px; }
  .benefit-list svg { flex: none; }
  .back-strip { position: absolute; left: 0; top: 283px; width: 337px; height: 8px; background: #222; }
  .back-brand { position: absolute; left: 0; top: 291px; width: 337px; height: 164px; background: linear-gradient(90deg, #ffffff 0%, #e4e4e4 100%); text-align: center; font-family: "Montserrat", sans-serif; }
  .back-brand .brand-name { font-size: 38px; margin-top: 24px; }
  .back-brand .brand-tagline { font-size: 15px; margin-top: 10px; }
  .back-brand .phone { font-size: 21px; font-weight: 700; color: var(--phone-red); margin-top: 10px; display: flex; justify-content: center; align-items: center; gap: 5px; }
  .back-brand .email { font-size: 11px; font-weight: 600; margin-top: 6px; }
  .back-brand .web { font-size: 11px; font-weight: 500; margin-top: 3px; }
  .back-brand .web span { color: var(--phone-red); }

  .stamp-box { position: absolute; left: 561px; top: 27px; width: 86px; height: 101px; border: 1px solid var(--rule); }
  .address-line { position: absolute; left: 392px; width: 256px; border-top: 1px solid var(--rule); }
  .address-line--1 { top: 205px; }
  .address-line--2 { top: 282px; }
</style>
</head>
<body>

<section class="card card--front">
  <header class="front-header">
    <div class="brand-name">Louver Crest</div>
    <div class="brand-tagline">Houston's Source for Plantation Shutters</div>
  </header>
  <div class="front-contact">
    <div class="cta">Call Us Today for Free Consultation!</div>
    <div class="phone">281.555.7384</div>
    <div class="web">www.<span>louvercresthouston</span>.example</div>
  </div>

  <div class="front-panel">
    <div class="front-photo" role="img" aria-label="Dining room with live-edge wood table, upholstered chairs, chandelier and dark plantation shutters"></div>
    <svg class="front-curve" width="340" height="345" viewBox="0 0 340 345" aria-hidden="true">
      <path d="M0 0 H335 C300 40 285 110 288 180 C291 250 300 310 310 345 H0 Z" fill="#a3352b"/>
      <path d="M0 0 H318 C285 45 272 115 275 185 C278 255 285 310 292 345 H0 Z" fill="#2a2322"/>
    </svg>
    <div class="front-copy">
      <p>Dale Whitcombe owner has been manufacturing shutters for over 44 years in the Houston area.</p>
      <p>After you make an appointment, our staff will come to your home to make precise measurements of each window.</p>
      <p>All shutters are manufactured in our Houston plant, so you know that your shutters will be ready for installation in a timely fashion.</p>
    </div>
    <div class="front-divider"></div>
    <p class="front-warranty">All plantation shutters come with a<br><strong>Limited Lifetime Warranty.</strong><br>If you have a problem, <strong>we will fix it.</strong></p>
  </div>
</section>

<section class="card card--back">
  <div class="back-photo" role="img" aria-label="Study room with arched windows fitted with white plantation shutters"></div>
  <div class="back-band">
    <h3>Call today to see what we are all about:</h3>
    <ul class="benefit-list">
      <li><svg width="12" height="11" viewBox="0 0 12 11"><path d="M1 6 L4.5 9.5 L11 1" stroke="#fff" stroke-width="2" fill="none"/></svg>Industry Leading Plantation Shutter Manufacturer</li>
      <li><svg width="12" height="11" viewBox="0 0 12 11"><path d="M1 6 L4.5 9.5 L11 1" stroke="#fff" stroke-width="2" fill="none"/></svg>Quick Turnaround</li>
      <li><svg width="12" height="11" viewBox="0 0 12 11"><path d="M1 6 L4.5 9.5 L11 1" stroke="#fff" stroke-width="2" fill="none"/></svg>Limited Lifetime Warranty</li>
      <li><svg width="12" height="11" viewBox="0 0 12 11"><path d="M1 6 L4.5 9.5 L11 1" stroke="#fff" stroke-width="2" fill="none"/></svg>And much, much more!</li>
    </ul>
  </div>
  <div class="back-strip"></div>
  <div class="back-brand">
    <div class="brand-name">Louver Crest</div>
    <div class="brand-tagline">Houston's Source for Plantation Shutters</div>
    <div class="phone">
      <svg width="16" height="16" viewBox="0 0 16 16" aria-hidden="true"><circle cx="8" cy="8" r="7" fill="none" stroke="#222" stroke-width="1.4"/><path d="M5.5 4.5 L7 6 L6.2 7 C6.8 8.3 7.7 9.2 9 9.8 L10 9 L11.5 10.5 L10.5 11.6 C7.5 11.2 4.8 8.5 4.4 5.5 Z" fill="#222"/></svg>
      281.555.7384
    </div>
    <div class="email">louvercrest@mailnest.example</div>
    <div class="web">www.<span>louvercresthouston</span>.example</div>
  </div>

  <div class="stamp-box"></div>
  <div class="address-line address-line--1"></div>
  <div class="address-line address-line--2"></div>
</section>

</body>
</html>
```